Display ads - Med spa Velmira promotion

Please create an ad creative for a promotional special for a med spa:
First-time customers who book a Velmira appointment receive $50 off the Velmira treatment

Please have an aspect of diversity in the ad (the company is black and woman-owned, so more than just white people in the ad creative

The company goes for "clean and tranquil" as part of their aesthetic

Attached here are the logo and picture of the homepage, and other images on the website, typical of the aesthetic of the company identity

you can find the website here for inspiration: thedewlinestudioct.com

Please no "black and white" photography, full color only, thank you!

Target Market(s)

New Haven, Connecticut, wealthy individuals who want to look and feel younger, want great skin, and want to feel youthful

Industry/Entity Type

Medspa/beauty

Requirements
Must have
• Need 5 sizes that fit the following Medium rectangle: 300×250; Large rectangle: 300×600 ; 728x90, 300x50; 160x600
Nice to have
• Clean, refined, bright
Should not have
• black and white photos, cartoonish, or drawn items

```html
<!DOCTYPE html>
<html lang="en">
<head>
<meta charset="utf-8">
<title>The Dewline Studio – Velmira Display Ad Set</title>
<link rel="stylesheet" href="https://fonts.googleapis.com/css2?family=Marcellus&family=Roboto:wght@400&display=swap">
<style>
  :root {
    --board: #5c5d5f;
    --label: #ffffff;
    --offer-blue: #1fa2dc;
    --stripe-blue: #18a0e2;
    --stripe-green: #b7d8b1;
    --ink: #2b2d36;
    --rule-rose: #e3a3a8;
    --sky-top: #eef0f0;
    --sky-mid: #e6edf0;
    --sky-low: #a8d3ef;
    --cta-fill: rgba(240, 242, 243, 0.92);
  }
  * { box-sizing: border-box; margin: 0; padding: 0; }
  html, body { width: 1200px; height: 645px; overflow: hidden; }
  body { background: var(--board); position: relative; font-family: "Marcellus", serif; color: var(--ink); }

  .size-label {
    position: absolute; font-family: "Roboto", sans-serif; color: var(--label);
    font-size: 25px; line-height: 1; transform: translateX(-50%); white-space: nowrap;
  }

  .ad {
    position: absolute; overflow: hidden;
    background: linear-gradient(180deg, var(--sky-top) 0%, var(--sky-mid) 45%, var(--sky-low) 100%);
  }
  .ad--wide { background: linear-gradient(180deg, var(--sky-top) 0%, var(--sky-mid) 50%, #c2e0f2 100%); }

  .corner { position: absolute; display: block; }

  .photo {
    position: absolute;
    background:
      radial-gradient(ellipse 22% 38% at 20% 62%, rgba(120,70,45,0.95), rgba(120,70,45,0) 100%),
      radial-gradient(ellipse 26% 42% at 50% 52%, rgba(226,160,135,0.95), rgba(226,160,135,0) 100%),
      radial-gradient(ellipse 30% 34% at 48% 18%, rgba(90,50,35,0.9), rgba(90,50,35,0) 100%),
      radial-gradient(ellipse 20% 36% at 78% 58%, rgba(205,150,120,0.85), rgba(205,150,120,0) 100%),
      radial-gradient(ellipse 16% 30% at 8% 35%, rgba(30,24,24,0.9), rgba(30,24,24,0) 100%),
      linear-gradient(90deg, rgba(170,120,95,0.35), rgba(170,120,95,0) 100%);
  }

  .offer { position: absolute; white-space: nowrap; text-align: center; }
  .offer__price { color: var(--offer-blue); line-height: 1; display: block; }
  .offer__price .amount { font-size: 1.2em; }
  .offer__item { display: block; line-height: 1.15; letter-spacing: 0.02em; }
  .offer__audience { display: block; letter-spacing: 0.14em; line-height: 1.3; }

  .benefits { position: absolute; list-style: none; white-space: nowrap; }
  .benefits li { display: flex; align-items: center; letter-spacing: 0.02em; }
  .benefits svg { flex: none; margin-right: 0.35em; width: 0.75em; height: 0.75em; }

  .cta {
    position: absolute; border-radius: 50%; background: var(--cta-fill);
    display: flex; align-items: center; justify-content: center; text-align: center;
    line-height: 0.95; letter-spacing: 0.03em; color: var(--ink);
  }

  .brand {
    position: absolute; display: flex; align-items: center; white-space: nowrap;
    font-family: "Marcellus", serif; color: var(--ink); line-height: 1;
  }
  .brand__dot { border-radius: 50%; background: var(--offer-blue); flex: none; }

  /* 300 x 250 */
  .ad--medium { left: 54px; top: 68px; width: 266px; height: 221px; }
  .ad--medium .photo { left: 0; top: 62px; width: 250px; height: 159px; }
  .ad--medium .offer { left: 22px; top: 14px; }
  .ad--medium .offer__price { font-size: 27px; }
  .ad--medium .offer__item { font-size: 9.5px; margin-top: 2px; }
  .ad--medium .offer__audience { font-size: 6px; }
  .ad--medium .benefits { left: 162px; top: 62px; font-size: 8.6px; line-height: 10.3px; }
  .ad--medium .cta { left: 187px; top: 138px; width: 68px; height: 68px; font-size: 16px; }
  .ad--medium .brand { left: 170px; top: 22px; font-size: 8px; }
  .ad--medium .brand__dot { width: 8px; height: 8px; margin-right: 4px; }

  /* 300 x 50 (small) */
  .ad--mobile { left: 370px; top: 125px; width: 266px; height: 44px; }
  .ad--mobile .photo { left: 0; top: 4px; width: 62px; height: 40px; }
  .ad--mobile .cta { left: 62px; top: 13px; width: 26px; height: 26px; font-size: 6px; }
  .ad--mobile .brand { left: 92px; top: 21px; font-size: 4px; }
  .ad--mobile .brand__dot { width: 4px; height: 4px; margin-right: 2px; }
  .ad--mobile .offer { left: 136px; top: 9px; }
  .ad--mobile .offer__price { font-size: 14px; }
  .ad--mobile .offer__item { font-size: 4.6px; }
  .ad--mobile .offer__audience { font-size: 3.2px; }
  .ad--mobile .benefits { left: 199px; top: 15px; font-size: 5px; line-height: 6.3px; }

  /* 728 x 90 */
  .ad--leader { left: 370px; top: 221px; width: 645px; height: 68px; }
  .ad--leader .photo { left: 0; top: 5px; width: 100px; height: 63px; }
  .ad--leader .brand { left: 120px; top: 29px; font-size: 9px; }
  .ad--leader .brand__dot { width: 9px; height: 9px; margin-right: 4px; }
  .ad--leader .offer { left: 215px; top: 10px; }
  .ad--leader .offer__price { font-size: 27px; }
  .ad--leader .offer__item { font-size: 9.3px; margin-top: 1px; }
  .ad--leader .offer__audience { font-size: 6px; }
  .ad--leader .benefits { left: 336px; top: 13px; font-size: 12.5px; line-height: 15px; }
  .ad--leader .cta { left: 494px; top: 9px; width: 48px; height: 48px; font-size: 11px; }

  /* 300 x 600 */
  .ad--large { left: 54px; top: 347px; width: 532px; height: 266px; }
  .ad--large .photo { left: 0; top: 46px; width: 385px; height: 220px; }
  .ad--large .brand { left: 36px; top: 32px; font-size: 12px; }
  .ad--large .brand__dot { width: 11px; height: 11px; margin-right: 5px; }
  .ad--large .offer { left: 316px; top: 19px; }
  .ad--large .offer__price { font-size: 46px; }
  .ad--large .offer__item { font-size: 16px; margin-top: 4px; padding-bottom: 2px; border-bottom: 0.7px solid var(--rule-rose); }
  .ad--large .offer__audience { font-size: 9.8px; margin-top: 3px; }
  .ad--large .benefits { left: 342px; top: 122px; font-size: 15px; line-height: 17.8px; }
  .ad--large .cta { left: 339px; top: 180px; width: 74px; height: 74px; font-size: 17px; }

  /* 160 x 600 */
  .ad--skyscraper { left: 629px; top: 470px; width: 532px; height: 141px; }
  .ad--skyscraper .photo { left: 0; top: 10px; width: 205px; height: 131px; }
  .ad--skyscraper .cta { left: 188px; top: 53px; width: 73px; height: 73px; font-size: 17px; }
  .ad--skyscraper .offer { left: 271px; top: 14px; }
  .ad--skyscraper .offer__price { font-size: 35px; }
  .ad--skyscraper .offer__item { font-size: 12px; margin-top: 3px; padding-bottom: 1px; border-bottom: 0.6px solid var(--rule-rose); }
  .ad--skyscraper .offer__audience { font-size: 7.3px; margin-top: 2px; }
  .ad--skyscraper .benefits { left: 270px; top: 86px; font-size: 12.5px; line-height: 15px; }
  .ad--skyscraper .brand { left: 424px; top: 67px; font-size: 9px; }
  .ad--skyscraper .brand__dot { width: 9px; height: 9px; margin-right: 4px; }
</style>
</head>
<body>
<svg width="0" height="0" style="position:absolute" aria-hidden="true">
  <symbol id="tick" viewBox="0 0 12 12">
    <circle cx="6" cy="6" r="5" fill="none" stroke="currentColor" stroke-width="1.2"/>
    <path d="M3.6 6.2 L5.4 7.9 L8.6 4.3" fill="none" stroke="currentColor" stroke-width="1.2" stroke-linecap="round" stroke-linejoin="round"/>
  </symbol>
</svg>

<!-- Medium rectangle -->
<div class="size-label" style="left:183px; top:36px;">300 x 250</div>
<section class="ad ad--medium">
  <svg class="corner" style="right:0; top:0; width:70px; height:45px;" viewBox="0 0 100 100" preserveAspectRatio="none">
    <polygon points="25,0 42,0 100,62 100,90" fill="var(--stripe-blue)" opacity="0.55"/>
    <polygon points="50,0 100,0 100,50" fill="var(--stripe-green)"/>
  </svg>
  <svg class="corner" style="left:0; top:0; width:40px; height:22px;" viewBox="0 0 100 100" preserveAspectRatio="none">
    <polygon points="0,0 100,0 0,100" fill="var(--stripe-green)"/>
  </svg>
  <div class="photo" role="img" aria-label="Three smiling women of different skin tones posing cheek to cheek"></div>
  <div class="offer">
    <span class="offer__price"><span class="amount">$50</span> OFF</span>
    <span class="offer__item">A VELMIRA TREATMENT</span>
    <span class="offer__audience">FOR FIRST TIME CUSTOMER</span>
  </div>
  <div class="brand"><span class="brand__dot"></span>The Dewline Studio</div>
  <ul class="benefits">
    <li><svg><use href="#tick"/></svg>RELIEVE MIGRAINES</li>
    <li><svg><use href="#tick"/></svg>SMOOTH LINES</li>
    <li><svg><use href="#tick"/></svg>FEEL RENEWED</li>
  </ul>
  <div class="cta">BOOK<br>HERE</div>
</section>

<!-- Mobile banner -->
<div class="size-label" style="left:489px; top:96px;">300x50</div>
<section class="ad ad--mobile ad--wide">
  <svg class="corner" style="right:0; top:0; width:60px; height:12px;" viewBox="0 0 100 100" preserveAspectRatio="none">
    <polygon points="0,0 25,0 100,85 100,100" fill="var(--stripe-blue)"/>
    <polygon points="40,0 100,0 100,60" fill="var(--stripe-green)"/>
  </svg>
  <div class="photo" role="img" aria-label="Three smiling women of different skin tones posing cheek to cheek"></div>
  <div class="cta">BOOK<br>HERE</div>
  <div class="brand"><span class="brand__dot"></span>The Dewline Studio</div>
  <div class="offer">
    <span class="offer__price"><span class="amount">$50</span> OFF</span>
    <span class="offer__item">A VELMIRA TREATMENT</span>
    <span class="offer__audience">FOR FIRST TIME CUSTOMER</span>
  </div>
  <ul class="benefits">
    <li><svg><use href="#tick"/></svg>RELIEVE MIGRAINES</li>
    <li><svg><use href="#tick"/></svg>SMOOTH LINES</li>
    <li><svg><use href="#tick"/></svg>FEEL RENEWED</li>
  </ul>
</section>

<!-- Leaderboard -->
<div class="size-label" style="left:489px; top:187px;">300x50</div>
<section class="ad ad--leader ad--wide">
  <svg class="corner" style="right:0; bottom:0; width:125px; height:46px;" viewBox="0 0 100 100" preserveAspectRatio="none">
    <polygon points="100,0 100,30 8,100 0,100" fill="var(--stripe-blue)"/>
    <polygon points="100,48 100,100 35,100" fill="var(--stripe-green)"/>
  </svg>
  <div class="photo" role="img" aria-label="Three smiling women of different skin tones posing cheek to cheek"></div>
  <div class="brand"><span class="brand__dot"></span>The Dewline Studio</div>
  <div class="offer">
    <span class="offer__price"><span class="amount">$50</span> OFF</span>
    <span class="offer__item">A VELMIRA TREATMENT</span>
    <span class="offer__audience">FOR FIRST TIME CUSTOMER</span>
  </div>
  <ul class="benefits">
    <li><svg><use href="#tick"/></svg>RELIEVE MIGRAINES</li>
    <li><svg><use href="#tick"/></svg>SMOOTH LINES</li>
    <li><svg><use href="#tick"/></svg>FEEL RENEWED</li>
  </ul>
  <div class="cta">BOOK<br>HERE</div>
</section>

<!-- Large rectangle -->
<div class="size-label" style="left:183px; top:317px;">300 x 600</div>
<section class="ad ad--large">
  <svg class="corner" style="left:0; top:0; width:52px; height:34px;" viewBox="0 0 100 100" preserveAspectRatio="none">
    <polygon points="0,60 100,0 70,0 0,40" fill="var(--stripe-blue)"/>
    <polygon points="0,0 48,0 0,30" fill="var(--stripe-green)"/>
  </svg>
  <svg class="corner" style="right:0; bottom:0; width:145px; height:66px;" viewBox="0 0 100 100" preserveAspectRatio="none">
    <polygon points="100,0 100,30 8,100 0,100" fill="var(--stripe-blue)"/>
    <polygon points="100,52 100,100 32,100" fill="var(--stripe-green)"/>
  </svg>
  <div class="photo" role="img" aria-label="Three smiling women of different skin tones posing cheek to cheek"></div>
  <div class="brand"><span class="brand__dot"></span>The Dewline Studio</div>
  <div class="offer">
    <span class="offer__price"><span class="amount">$50</span> OFF</span>
    <span class="offer__item">A VELMIRA TREATMENT</span>
    <span class="offer__audience">FOR FIRST TIME CUSTOMER</span>
  </div>
  <ul class="benefits">
    <li><svg><use href="#tick"/></svg>RELIEVE MIGRAINES</li>
    <li><svg><use href="#tick"/></svg>SMOOTH LINES</li>
    <li><svg><use href="#tick"/></svg>FEEL RENEWED</li>
  </ul>
  <div class="cta">BOOK<br>HERE</div>
</section>

<!-- Wide skyscraper -->
<div class="size-label" style="left:873px; top:435px;">160 x 600</div>
<section class="ad ad--skyscraper ad--wide">
  <svg class="corner" style="right:0; top:0; width:96px; height:38px;" viewBox="0 0 100 100" preserveAspectRatio="none">
    <polygon points="0,0 22,0 100,75 100,100" fill="var(--stripe-blue)"/>
    <polygon points="42,0 100,0 100,48" fill="var(--stripe-green)"/>
  </svg>
  <svg class="corner" style="right:0; bottom:0; width:96px; height:38px;" viewBox="0 0 100 100" preserveAspectRatio="none">
    <polygon points="100,0 100,30 8,100 0,100" fill="var(--stripe-blue)"/>
    <polygon points="100,52 100,100 32,100" fill="var(--stripe-green)"/>
  </svg>
  <div class="photo" role="img" aria-label="Three smiling women of different skin tones posing cheek to cheek"></div>
  <div class="cta">BOOK<br>HERE</div>
  <div class="offer">
    <span class="offer__price"><span class="amount">$50</span> OFF</span>
    <span class="offer__item">A VELMIRA TREATMENT</span>
    <span class="offer__audience">FOR FIRST TIME CUSTOMER</span>
  </div>
  <ul class="benefits">
    <li><svg><use href="#tick"/></svg>RELIEVE MIGRAINES</li>
    <li><svg><use href="#tick"/></svg>SMOOTH LINES</li>
    <li><svg><use href="#tick"/></svg>FEEL RENEWED</li>
  </ul>
  <div class="brand"><span class="brand__dot"></span>The Dewline Studio</div>
</section>
</body>
</html>
```